Velvet Basin Suites, a portable luxury restroom trailer company needs a landing page

We need a landing page for a luxury portable restroom trailer company. This should be modern, and simple - use any combination of Pantone colors: Warm Gray 1C, Black 7C, 7529c, 873C, 8003C

We rent these trailers for special events like weddings, private parties, festivals, family reunions, team building, wine tastings, beer tastings, food truck round-ups, etc.

An idea of the landing page is in the files below. Please use stock photography and placeholder text for now. The winning design will be given final content.

Requirements
Must have
• Multiple "Get Quote" buttons or a place for them to type in type of rental, how many people etc

```html
<!DOCTYPE html>
<html lang="en">
<head>
<meta charset="utf-8">
<title>Velvet Basin Suites</title>
<link rel="stylesheet" href="https://fonts.googleapis.com/css2?family=Montserrat:wght@400;500;600;700&family=Playfair+Display:wght@700;900&display=swap">
<style>
:root{
  --blue:#1a44a8;
  --navy:#172856;
  --warm:#f2eeee;
  --ink:#333;
  --muted:#555;
  --lav:#c8c4ee;
  --white:#fff;
}
*{box-sizing:border-box;margin:0;padding:0}
html,body{width:1200px;height:3728px;overflow:hidden}
body{position:relative;font-family:'Montserrat',sans-serif;color:var(--ink);background:var(--white)}
.abs{position:absolute}
.btn{position:absolute;background:var(--blue);color:var(--white);font-size:13px;letter-spacing:1.5px;display:flex;align-items:center;justify-content:center;border-radius:3px;box-shadow:0 3px 6px rgba(26,68,168,.35)}

/* header */
.site-header{position:absolute;left:0;top:0;width:1200px;height:80px;background:var(--white);border-bottom:2px solid var(--navy)}
.brand{position:absolute;left:126px;top:12px;font-family:'Playfair Display',serif;font-weight:700;color:var(--blue);line-height:1}
.brand .l1{font-size:28px;letter-spacing:4px}
.brand .l2{font-size:14px;letter-spacing:4px;margin-top:6px}
.nav a{position:absolute;top:32px;font-size:13px;color:#222;text-decoration:none}

/* hero */
.hero{position:absolute;left:0;top:80px;width:1200px;height:620px;background:linear-gradient(135deg,#2d3f66 0%,#1e3e6e 40%,#254a6a 60%,#1a2a52 100%)}
.hero-text{position:absolute;left:0;width:1200px;text-align:center;color:var(--white)}
.hero .w{top:200px;font-size:22px;letter-spacing:14px;font-weight:500}
.hero .big{top:240px;font-family:'Playfair Display',serif;font-weight:900;font-size:104px;letter-spacing:34px;padding-left:34px}
.hero .sub{top:380px;font-family:'Playfair Display',serif;font-weight:900;font-size:46px;letter-spacing:18px;padding-left:18px}

/* sections */
.h2{position:absolute;font-size:64px;font-weight:600;color:var(--blue);line-height:1}
.lead{position:absolute;font-size:12px;line-height:17px;color:var(--muted)}

.event-card{position:absolute;top:921px;width:180px;height:267px;border-radius:3px;overflow:hidden}
.event-card .ph{position:absolute;inset:0}
.event-card .shade{position:absolute;left:0;bottom:0;width:100%;height:90px;background:linear-gradient(transparent,rgba(0,0,0,.85))}
.event-card .name{position:absolute;left:19px;bottom:14px;font-size:16px;font-weight:600;color:var(--white)}
.event-card.active{background:var(--blue);box-shadow:0 8px 14px rgba(26,68,168,.4);color:var(--white)}
.event-card.active h3{position:absolute;right:16px;top:22px;font-size:16px;font-weight:600}
.event-card.active p{position:absolute;left:16px;top:50px;width:152px;font-size:12px;line-height:19.5px}
.event-card.active a{position:absolute;right:16px;top:226px;font-size:11px;color:var(--white)}

.products{position:absolute;left:0;top:1271px;width:1200px;height:1251px;background:var(--warm)}
.product{position:absolute;left:126px;width:949px;height:279px;background:var(--white)}
.product.featured{box-shadow:0 0 0 2px var(--lav),0 4px 12px rgba(80,70,200,.15)}
.product h3{position:absolute;left:30px;top:28px;font-size:21px;font-weight:600;color:#333}
.product.featured h3,.product.featured a{color:var(--blue)}
.product p{position:absolute;left:31px;top:66px;width:505px;font-size:15.5px;line-height:22px;color:var(--muted)}
.product a{position:absolute;left:31px;top:192px;font-size:15px;color:#333}
.product .ph{position:absolute;left:599px;top:15px;width:337px;height:250px}

.toll{position:absolute;left:666px;top:2614px;width:409px;height:111px;border:2px solid var(--lav);background:var(--white)}
.toll .t1{position:absolute;left:168px;top:28px;font-size:17px;color:#444}
.toll .t2{position:absolute;left:122px;top:52px;font-size:26px;font-weight:700;color:var(--blue)}

.quote{position:absolute;left:481px;top:2756px;width:594px;height:411px;background:var(--blue)}
.quote h3{position:absolute;left:0;top:54px;width:100%;text-align:center;color:var(--white);font-size:20px;font-weight:700}
.field{position:absolute;height:32px;border:1px solid #2d57c0;background:#1e49b0;color:#b9c8ee;font-size:12px;padding-left:14px;display:flex;align-items:center}
.field svg{position:absolute;right:10px;top:9px}
.submit{position:absolute;left:24px;top:306px;width:545px;height:43px;border:1.5px solid #4d74d4;color:#b9c8ee;font-size:14px;letter-spacing:4px;display:flex;align-items:center;justify-content:center;gap:26px}

/* footer */
.footer{position:absolute;left:0;top:3324px;width:1200px;height:314px;background:var(--navy);color:var(--white)}
.footer .brand{left:126px;top:48px;color:#3a5fd0}
.footer .brand .l1{font-size:48px;letter-spacing:6px}
.footer .brand .l2{font-size:22px;letter-spacing:8px;color:var(--white);margin-top:10px}
.fh{position:absolute;font-size:19px;font-weight:500}
.flink{position:absolute;font-size:17px}
.social{position:absolute;left:959px;font-size:14px;display:flex;align-items:center;gap:10px}
.social span.c{width:25px;height:25px;border:1.5px solid var(--white);border-radius:50%}
.copy{position:absolute;left:0;top:3638px;width:1200px;height:90px;background:var(--blue);color:var(--white);font-size:16px;font-weight:500;display:flex;align-items:center;justify-content:center}
</style>
</head>
<body>

<header class="site-header">
  <div class="brand"><div class="l1">VELVET</div><div class="l2">BASIN SUITES</div></div>
  <nav class="nav">
    <a style="left:768px">EVENT</a>
    <a style="left:845px">PRODUCTS</a>
  </nav>
  <div class="btn" style="left:954px;top:25px;width:121px;height:32px">CONTACT</div>
</header>

<section class="hero" role="img" aria-label="Collage of portable restroom units and restroom trailers under a navy overlay">
  <div class="hero-text w">WELCOME TO</div>
  <div class="hero-text big">VELVET</div>
  <div class="hero-text sub">BASIN SUITES</div>
</section>

<section class="events">
  <h2 class="h2" style="left:122px;top:778px">Events</h2>
  <p class="lead" style="left:126px;top:850px;width:650px">Sed ut perspiciatis unde omnis iste natus error sit voluptatem accusantium doloremque laudantium, totam rem aperiam, eaque ipsa quae ab illo inventore veritatis et quasi architecto beatae vitae dicta sunt explicabo. Nemo enim ipsam voluptatem quia voluptas sit aspernatur aut odit aut fugit,</p>
  <div class="btn" style="left:954px;top:824px;width:121px;height:31px">VIEW MORE</div>

  <div class="event-card" style="left:126px"><div class="ph" role="img" aria-label="Wedding bouquet of white roses" style="background:linear-gradient(160deg,#2a3550,#d9dcd4 55%,#4a5a40)"></div><div class="shade"></div><div class="name">Weddings</div></div>
  <div class="event-card" style="left:318px"><div class="ph" role="img" aria-label="Crowd dancing under blue stage lights" style="background:linear-gradient(160deg,#4fa0ff,#1240c8 55%,#06123a)"></div><div class="shade"></div><div class="name">Private Parties</div></div>
  <div class="event-card active" style="left:511px"><h3>Festivals</h3><p>Sed ut perspiciatis unde omnis iste natus error sit voluptatem accusantium doloremque laudantium, totam rem aperiam, eaque ipsa quae ab illo inventore veritatis et quasi architecto</p><a>Learn More</a></div>
  <div class="event-card" style="left:703px"><div class="ph" role="img" aria-label="Family group in white outfits by a lake" style="background:linear-gradient(180deg,#a9c4d6,#5e7f5a 45%,#e8e4de 75%)"></div><div class="shade"></div><div class="name">Family Reunions</div></div>
  <div class="event-card" style="left:896px"><div class="ph" role="img" aria-label="Guests toasting at an outdoor wine tasting" style="background:linear-gradient(160deg,#e5b760,#8a7a5a 50%,#3a3a38)"></div><div class="shade"></div><div class="name">Wine Tastings</div></div>
</section>

<section class="products">
  <h2 class="h2" style="left:0;top:87px;width:1200px;text-align:center">Products</h2>
  <p class="lead" style="left:280px;top:159px;width:640px;text-align:center">Sed ut perspiciatis unde omnis iste natus error sit voluptatem accusantium doloremque laudantium, totam rem aperiam, eaque ipsa quae ab illo inventore veritatis et quasi architecto beatae</p>
</section>

<article class="product" style="top:1488px"><h3>Product Name Here</h3><p>Sed ut perspiciatis unde omnis iste natus error sit voluptatem accusantium doloremque laudantium, totam rem aperiam, eaque ipsa quae ab illo inventore veritatis et quasi architecto beatae vitae dicta sunt explicabo. Nemo enim ipsam voluptatem quia voluptas sit aspernatur aut odit aut fugit,</p><a>Learn More &gt;</a><div class="ph" role="img" aria-label="White and orange portable toilets standing in a grassy field" style="background:linear-gradient(180deg,#c9d8e6,#b9a27a 45%,#5f9a3a 70%)"></div></article>
<article class="product featured" style="top:1780px"><h3>Product Name Here</h3><p>Sed ut perspiciatis unde omnis iste natus error sit voluptatem accusantium doloremque laudantium, totam rem aperiam, eaque ipsa quae ab illo inventore veritatis et quasi architecto beatae vitae dicta sunt explicabo. Nemo enim ipsam voluptatem quia voluptas sit aspernatur aut odit aut fugit,</p><a>Learn More &gt;</a><div class="ph" role="img" aria-label="Light blue portable toilet in front of green trees" style="background:linear-gradient(90deg,#2f4a22,#7fb2e0 35%,#7fb2e0 55%,#3b5a26)"></div></article>
<article class="product" style="top:2072px"><h3>Product Name Here</h3><p>Sed ut perspiciatis unde omnis iste natus error sit voluptatem accusantium doloremque laudantium, totam rem aperiam, eaque ipsa quae ab illo inventore veritatis et quasi architecto beatae vitae dicta sunt explicabo. Nemo enim ipsam voluptatem quia voluptas sit aspernatur aut odit aut fugit,</p><a>Learn More &gt;</a><div class="ph" role="img" aria-label="Long row of red portable toilets" style="background:linear-gradient(90deg,#c8344a,#d94a5c 70%,#6a8a4a)"></div></article>
<div class="btn" style="left:540px;top:2398px;width:121px;height:32px">VIEW MORE</div>

<section class="contact">
  <h2 class="h2" style="left:122px;top:2608px">Contact Us</h2>
  <p class="lead" style="left:126px;top:2680px;width:520px">Sed ut perspiciatis unde omnis iste natus error sit voluptatem accusantium doloremque laudantium, totam rem aperiam, eaque ipsa quae ab illo inventore</p>
  <div class="toll">
    <svg class="abs" style="left:62px;top:38px" width="40" height="40" viewBox="0 0 24 24"><path fill="#1a44a8" d="M6.6 10.8a15.1 15.1 0 006.6 6.6l2.2-2.2a1 1 0 011-.25 11.4 11.4 0 003.6.57 1 1 0 011 1V20a1 1 0 01-1 1A17 17 0 013 4a1 1 0 011-1h3.5a1 1 0 011 1c0 1.25.2 2.45.57 3.57a1 1 0 01-.25 1z"/></svg>
    <div class="t1">TOLL FREE</div>
    <div class="t2">+555 010 2020</div>
  </div>
  <div class="abs" role="img" aria-label="Blue and pink portable restroom units side by side" style="left:85px;top:2760px;width:396px;height:415px;background:linear-gradient(90deg,#2e6fd8,#3f8af0 55%,#e8578e 80%,#f07aa8)"></div>

  <form class="quote">
    <h3>CONTACT US FOR A QUOTE</h3>
    <div class="field" style="left:24px;top:104px;width:268px">Name</div>
    <div class="field" style="left:299px;top:104px;width:270px">Email</div>
    <div class="field" style="left:24px;top:144px;width:268px">Phone</div>
    <div class="field" style="left:299px;top:144px;width:270px">Type of Event?<svg width="14" height="14" viewBox="0 0 14 14"><circle cx="7" cy="7" r="6.5" fill="#b9c8ee"/><path d="M4 6l3 3 3-3" stroke="#1e49b0" stroke-width="1.6" fill="none"/></svg></div>
    <div class="field" style="left:24px;top:185px;width:268px">How many people?<svg width="14" height="14" viewBox="0 0 14 14"><circle cx="7" cy="7" r="6.5" fill="#b9c8ee"/><path d="M4 6l3 3 3-3" stroke="#1e49b0" stroke-width="1.6" fill="none"/></svg></div>
    <div class="field" style="left:299px;top:185px;width:270px">Type of product you're intrested In?<svg width="14" height="14" viewBox="0 0 14 14"><circle cx="7" cy="7" r="6.5" fill="#b9c8ee"/><path d="M4 6l3 3 3-3" stroke="#1e49b0" stroke-width="1.6" fill="none"/></svg></div>
    <div class="field" style="left:24px;top:225px;width:268px">When do you Need It?<svg width="14" height="14" viewBox="0 0 14 14"><circle cx="7" cy="7" r="6.5" fill="#b9c8ee"/><path d="M4 6l3 3 3-3" stroke="#1e49b0" stroke-width="1.6" fill="none"/></svg></div>
    <div class="field" style="left:299px;top:225px;width:270px">For How Long?<svg width="14" height="14" viewBox="0 0 14 14"><circle cx="7" cy="7" r="6.5" fill="#b9c8ee"/><path d="M7 3.5V7l2 1.5" stroke="#1e49b0" stroke-width="1.6" fill="none"/></svg></div>
    <div class="field" style="left:24px;top:265px;width:545px">Where?<svg width="14" height="14" viewBox="0 0 14 14"><circle cx="7" cy="7" r="6.5" fill="#b9c8ee"/><path d="M4 6l3 3 3-3" stroke="#1e49b0" stroke-width="1.6" fill="none"/></svg></div>
    <div class="submit">SUBMIT NOW <svg width="16" height="16" viewBox="0 0 16 16"><circle cx="8" cy="8" r="7.5" fill="#b9c8ee"/><path d="M5 8h6M8.5 5l3 3-3 3" stroke="#1e49b0" stroke-width="1.7" fill="none"/></svg></div>
  </form>
</section>

<footer class="footer">
  <div class="brand"><div class="l1">VELVET</div><div class="l2">BASIN SUITES</div></div>
  <div class="fh" style="left:126px;top:179px;font-size:18px">CONTACT</div>
  <div class="flink" style="left:126px;top:204px;font-size:17px">hello@velvetbasin.example</div>

  <div class="fh" style="left:420px;top:66px">SIGN UP FOR NEWSLETTER</div>
  <div class="abs" style="left:418px;top:113px;width:286px;height:38px;background:var(--white);border-radius:3px;color:#777;font-size:13px;padding:12px 0 0 18px">Enter email</div>
  <div class="btn" style="left:420px;top:164px;width:139px;height:36px;font-size:14px;letter-spacing:0;box-shadow:none">SUBSCRIBE</div>

  <div class="fh" style="left:772px;top:60px">QUICK LINKS</div>
  <div class="flink" style="left:772px;top:99px">Home</div>
  <div class="flink" style="left:772px;top:127px">Event</div>
  <div class="flink" style="left:772px;top:155px">Products</div>
  <div class="flink" style="left:772px;top:183px">Contact</div>

  <div class="fh" style="left:959px;top:60px">FOLLOW US</div>
  <div class="social" style="top:106px"><span class="c"></span>Pinboard</div>
  <div class="social" style="top:141px"><span class="c"></span>Chirper</div>
  <div class="social" style="top:177px"><span class="c"></span>Circlet</div>
  <div class="social" style="top:212px"><span class="c"></span>Reelcast</div>
</footer>
<div class="copy">Velvet Basin Suites (c) 2022 | All Rights Reserved.</div>

</body>
</html>
```